Lantern over the Harbor ~ A Widening Passage for Writers

My book is called “Lantern over the Harbor.” Its subtitle is “A Widening Passage for Writers.” It is a book about being a poet, writing poetry, and the ways in which poets are connected to both society and the central energy of the Universe. I want the cover design to be abstract and impressionistic. A suggestion of fireworks or a starburst would be a plus. To be consistent with the 3 other books I have published, I want the font for the title, as well as my name (Dorothea Quillbrake) to be Papyrus. The subtitle font can be something more plain and sans serif, like Arial or Franklin Gothic Book, probably in italics. As for color, I definitely want pale gold (angelic). Possible other complimentary colors could be either light or dark shades of gray, turquoise, rose, rust or red. I'm attaching the back cover text and also three pages from inside the book that have line drawings, to give an example of the interior artwork.
Updates

Forgot to mention: My book is a paperback. Its size will be 8.5" high and 5.5" wide. I'm self-publishing it, and it will be printed by Halvern Printworks in Nebraska, USA. It has 104 pages. I think you need the number of pages, in order to make the spine of the book the correct width.

Target Market(s)

My target market is people who write poetry or are interested in how poetry is written.

Industry/Entity Type

Poetry

Font styles to use
Sans Serif
Other font styles liked:
• Papyrus for the front cover. Arial or another sans serif font on the back cover.

Colors

Designer to choose colors to be used in the design.

Requirements
Must have
• My book cover needs to be inspiring and uplifting, as well as abstract and impressionistic, with kind of a "New Age" feel. I don't want anything that looks rigid and scholarly.
Nice to have
• The book talks about the connection poets have to the Universe and the Creative Energy at the center of everything. The cover should convey that Energy.
Should not have
• My cover should not be realistic, logical or straight-laced. I want something that feels free, imaginative and unfettered.

```html
<!DOCTYPE html>
<html lang="en">
<head>
<meta charset="utf-8">
<title>Lantern over the Harbor – Cover Wrap</title>
<link rel="stylesheet" href="https://fonts.googleapis.com/css2?family=Macondo&family=Poppins:ital,wght@0,400;0,600;0,700;1,400&display=swap">
<style>
  :root {
    --backdrop: #b3b3b3;
    --paper: #fdf4f1;
    --ink: #2a2a2a;
    --rose: #e0506e;
    --teal: #5f9f9f;
    --blush: #e7a7ae;
    --gold: #f0d27a;
    --fold: #8d8585;
  }
  * { margin: 0; padding: 0; box-sizing: border-box; }
  html, body { width: 1200px; height: 903px; overflow: hidden; background: var(--backdrop); }
  .wrap {
    position: absolute; left: 53px; top: 56px; width: 1095px; height: 790px;
    background: var(--paper);
  }
  .panel { position: absolute; top: 0; height: 790px; }
  .back-cover { left: 0; width: 513px; }
  .spine { left: 513px; width: 68px; border-left: 1px solid var(--fold); border-right: 1px solid var(--fold); }
  .front-cover { left: 581px; width: 514px; }

  .title-face { font-family: "Macondo", "Papyrus", fantasy; color: var(--ink); font-weight: 400; }

  /* back cover */
  .corner-wing {
    position: absolute; left: 0; top: 0; width: 122px; height: 234px;
    background: radial-gradient(ellipse at 20% 40%, var(--blush) 0%, var(--teal) 45%, rgba(95,159,159,0.3) 70%, rgba(253,244,241,0) 85%);
    border-bottom-right-radius: 100% 90%;
  }
  .author-photo {
    position: absolute; left: 205px; top: 61px; width: 100px; height: 141px;
    background: linear-gradient(180deg, #b9b4a8 0%, #d9b8a6 55%, #4f9a86 100%);
  }
  .back-copy {
    position: absolute; left: 45px; top: 230px; width: 423px;
    font-family: "Poppins", Arial, sans-serif; color: var(--ink);
    font-size: 11.3px; line-height: 15.6px;
  }
  .back-copy p { margin-bottom: 15px; text-align: justify; text-align-last: center; }
  .back-copy .lead { font-weight: 600; font-size: 12.6px; text-align: center; line-height: 15.6px; }
  .back-copy .chapters-intro { font-weight: 600; font-size: 12.4px; text-align: center; margin-bottom: 12px; }
  .chapters {
    color: var(--rose); font-weight: 600; font-size: 16.6px; line-height: 18px;
    text-align: center !important; margin-bottom: 20px !important; letter-spacing: -0.2px;
  }
  .back-mark { position: absolute; left: 42px; top: 676px; width: 140px; }
  .back-mark .big { font-size: 36px; line-height: 32px; display: block; }
  .back-mark .small { font-size: 14px; display: block; margin-left: 30px; line-height: 12px; }
  .back-mark .one { margin-left: 22px; }

  /* spine */
  .spine-text {
    position: absolute; left: 12px; writing-mode: vertical-rl;
    font-size: 30px; line-height: 40px; white-space: nowrap;
  }
  .spine-title { top: 40px; }
  .spine-author { top: 580px; }

  /* front cover */
  .front-title { position: absolute; left: 0; top: 40px; width: 514px; text-align: center; }
  .front-title .word { display: block; font-size: 96px; line-height: 88px; }
  .front-title .joiner { display: block; font-size: 34px; line-height: 30px; }
  .wing-art {
    position: absolute; left: 97px; top: 269px; width: 432px; height: 426px; left: 97px;
  }
  .wing-art { left: 97px; }
  .wing-field {
    position: absolute; left: 0; top: 0; width: 432px; height: 426px;
    background:
      radial-gradient(ellipse 25% 30% at 30% 35%, rgba(240,210,122,0.8), rgba(240,210,122,0) 70%),
      radial-gradient(ellipse 25% 30% at 70% 35%, rgba(240,210,122,0.8), rgba(240,210,122,0) 70%),
      radial-gradient(ellipse 45% 50% at 25% 55%, var(--blush) 0%, var(--teal) 60%, rgba(95,159,159,0) 80%),
      radial-gradient(ellipse 45% 50% at 75% 55%, var(--blush) 0%, var(--teal) 60%, rgba(95,159,159,0) 80%);
  }
  .subtitle {
    position: absolute; left: 0; top: 332px; width: 514px; text-align: center;
    font-family: "Poppins", Arial, sans-serif; font-size: 17px; line-height: 22px; color: var(--ink);
  }
  .front-author { position: absolute; left: 0; top: 760px; width: 514px; text-align: center; font-size: 40px; line-height: 40px; transform: translateY(-52px); }
</style>
</head>
<body>
  <div class="wrap">
    <section class="panel back-cover">
      <div class="corner-wing" role="img" aria-label="Corner detail of watercolour wing feathers in rose and turquoise"></div>
      <div class="author-photo" role="img" aria-label="Portrait photograph of the author"></div>
      <div class="back-copy">
        <p class="lead">Lantern over the Harbor is indeed “A Widening Passage for Writers.” It is written by Dorothea Quillbrake, an exciting, imaginative voice in American poetry.</p>
        <p>In <strong>Lantern over the Harbor</strong>, Dorothea discusses the essential elements of poetry and the process of writing it. She offers an inspiring view of the mission of poets and their connection to both society and the larger forces in the Universe. Her book is motivational, refreshing and irrepressibly optimistic.</p>
        <p class="chapters-intro">The seven intriguing chapters in Lantern over the Harbor are</p>
        <p class="chapters">LIBERATION ~ EXPERIENCE ~ WORDS ~ POETRY ~<br>INTEGRITY ~ BEAUTY ~ CREATION</p>
        <p>For over 50 years, Dorothea has been a teacher of writing and poetry. Since 2007, she has published three books of her poems: <em>Mind the Garden Gate, The Pale Hem of Forever and The Wide Velvet Hush.</em> Her work overflows with her characteristically rich images and quirky metaphors. It runs the gamut from subtle eroticism to abject grief, from defiant rage to philosophical meditation, and from borderline blasphemy to lyrical fantasy.</p>
        <p>Dorothea has been called by critic Gerald Ashcombe “a poet to be reckoned with; bright, feisty, compassionate.” (The Valley Courier, Millbrook, PA). Author Clara Wendholt (“<em>Birchmoor</em>,” 2011) says Dorothea’s poetry is like “a perpetual Surprise Party ~ memorable, insightful and thematically fascinating.”</p>
      </div>
      <div class="back-mark title-face">
        <span class="big one">Lantern</span>
        <span class="small">over the</span>
        <span class="big">Harbor</span>
      </div>
    </section>

    <section class="panel spine">
      <span class="spine-text spine-title title-face">Lantern over the Harbor</span>
      <span class="spine-text spine-author title-face">Dorothea Quillbrake</span>
    </section>

    <section class="panel front-cover">
      <h1 class="front-title title-face">
        <span class="word">Lantern</span>
        <span class="joiner">over the</span>
        <span class="word">Harbor</span>
      </h1>
      <div class="wing-art" style="left:41px;top:269px;" role="img" aria-label="Pair of mirrored watercolour angel wings in rose, turquoise and pale gold flame tones">
        <div class="wing-field"></div>
      </div>
      <p class="subtitle">A<br>Widening<br>Passage<br>for Writers</p>
      <p class="front-author title-face">Dorothea Quillbrake</p>
    </section>
  </div>
</body>
</html>
```